| 希望する色 | 特になし・その他 追記事項: 周囲の景色に埋没しないような色合いを希望します。 |
戸建賃貸住宅6棟の計画「ミドリテラス・カサネル」の看板デザインの依頼です。 【 概要 】 全6棟の戸建賃貸住宅を建築中です。 建築地が住宅街の中にあり場所がわかりにくいため、大通りから見える場所へ看板を掲出したいと考えています。 周辺にある戸建賃貸住宅は規格モノを建てただけですが、地元工務店と組んで自然環境を重視した計画としました。 賃貸住宅でも環境重視の方、都市部から郊外へ引っ越しをしてくる方、などにアピールしたいと思っています。 シンプルかつデザイン性の高い看板デザインを募集します。 【 依頼内容 】 ・看板サイズ:横3,000mm × 縦2,000mm ・看板の素材:メッシュターポリン(予定) ・デザイン素材:計画名のロゴは用意したものを使用してください。他はお任せします。 ・デザイン内容:「戸建賃貸住宅」は明示してください。建築地案内は矢印程度で良いかと考えています。敷地レイアウトの明示は不要です。 ・デザインの利用について:看板への使用が主目的ですが、HPへの掲載、不動産仲介業者への配布等も行う場合があります。作成デザインを尊重し編集、合成、切り抜き等は原則行いません。他制限事項あればお知らせください。 【 契約金額(税抜) 】 70,000円(税別) ※契約金額(税込)からシステム利用料を差し引いた金額が、ワーカーさまの受取金額となります その他ご質問等ありましたら、気軽にお問い合わせください。 ご応募をお待ちしております! |
| https://fuyoreside.sitelume.jp | ||
シンプルでもバランスが良く看板の目的に合致したデザインでした。
沢山のご提案ありがとうございました。良い案が幾つもあり採用デザインを1つに絞るのは悩みました。また機会がありましたらよろしくお願いします。

```html
<!DOCTYPE html>
<html lang="ja">
<head>
<meta charset="utf-8">
<title>ミドリテラス・カサネル 看板</title>
<link href="https://fonts.googleapis.com/css2?family=Noto+Sans+JP:wght@500;700;900&display=swap" rel="stylesheet">
<style>
  :root {
    --page-bg: #eef0ec;
    --leaf-light: #c9df9e;
    --leaf-mid: #94c061;
    --panel: #ffffff;
    --ink: #2b2b2b;
    --accent-red: #d6262c;
    --accent-green: #3f8a35;
    --band-text: #ffffff;
  }
  * { margin: 0; padding: 0; box-sizing: border-box; }
  html, body {
    width: 1200px; height: 710px; overflow: hidden;
    background: var(--page-bg);
    font-family: "Noto Sans JP", sans-serif;
  }
  .canvas {
    width: 1200px; height: 710px;
    display: flex; align-items: center; justify-content: center;
  }
  .signboard {
    position: relative;
    width: 900px; height: 600px;
    overflow: hidden;
    box-shadow: 0 6px 20px rgba(0,0,0,.18);
  }
  .foliage-backdrop {
    position: absolute; inset: 0;
    background: linear-gradient(135deg, var(--leaf-light), var(--leaf-mid));
  }
  .message-panel {
    position: absolute;
    left: 60px; right: 60px; top: 60px; height: 370px;
    background: var(--panel);
    display: flex; flex-direction: column; align-items: center; justify-content: center;
    gap: 14px;
  }
  .tagline {
    font-weight: 900; font-size: 54px; letter-spacing: .02em; color: var(--ink); line-height: 1.2;
  }
  .tagline .highlight { color: var(--accent-red); }
  .headline {
    font-weight: 900; font-size: 108px; letter-spacing: .04em; color: var(--ink); line-height: 1.1;
  }
  .project-name {
    font-weight: 700; font-size: 36px; color: var(--accent-green); letter-spacing: .05em; line-height: 1.2;
  }
  .recruit-band {
    position: absolute;
    left: 60px; right: 60px; top: 450px; height: 70px;
    background: var(--accent-red);
    display: flex; align-items: center; justify-content: space-between;
    padding: 0 28px;
    color: var(--band-text);
  }
  .recruit-label { font-weight: 900; font-size: 36px; letter-spacing: .08em; line-height: 1; }
  .direction { display: flex; align-items: center; gap: 12px; font-weight: 700; font-size: 24px; line-height: 1; }
</style>
</head>
<body>
<main class="canvas">
  <section class="signboard">
    <div class="foliage-backdrop" role="img" aria-label="野菜と葉のイラスト背景"></div>
    <div class="message-panel">
      <p class="tagline"><span class="highlight">自然環境</span>を重視した</p>
      <h1 class="headline">戸建賃貸住宅</h1>
      <p class="project-name">ミドリテラス・カサネル</p>
    </div>
    <div class="recruit-band">
      <span class="recruit-label">入居者募集</span>
      <span class="direction">この先
        <svg width="150" height="34" viewBox="0 0 150 34" aria-hidden="true">
          <path d="M0 13 H122 V2 L150 17 L122 32 V21 H0 Z" fill="var(--band-text)"/>
        </svg>
      </span>
    </div>
  </section>
</main>
</body>
</html>
```